Website for Excavator and Earthworks Company

We require a modern, sleek and practical website for our newly created earthworks/excavator business in Perth, Western Australia called Gullwind Stonecut Earthworks.

The website should have a modern, cutting edge feel but only needs to be relatively simplistic in it's layout and eventual functionality.

Some pages it should have would be Home, About, Projects and Contact Us.

Number of Pages Required

1 page

```html
<!DOCTYPE html>
<html lang="en">
<head>
<meta charset="utf-8">
<title>Gullwind Stonecut Earthworks</title>
<link href="https://fonts.googleapis.com/css2?family=Inter:wght@400;500;600;700;800&display=swap" rel="stylesheet">
<style>
:root{
  --lime:#c9d82b;
  --ink:#161616;
  --bg:#1a1a1a;
  --card:#232323;
  --band:#26282a;
  --foot:#0e0e0e;
  --text:#ffffff;
  --muted:#9a9a9a;
  --dim:#6d6d6d;
  --line:#2e2e2e;
}
*{box-sizing:border-box;margin:0;padding:0}
html,body{width:1200px;height:2861px;overflow:hidden;background:#fff;font-family:'Inter',sans-serif;color:var(--text)}
.brand-board{position:absolute;left:344px;top:252px;width:512px;height:70px;display:flex;align-items:center;gap:18px}
.brand-board .mark{width:54px;height:54px;background:var(--lime)}
.brand-board .name{font-size:31px;font-weight:800;color:var(--ink);letter-spacing:1px;text-transform:uppercase;line-height:1}

.site{position:absolute;left:126px;top:552px;width:948px;height:2178px;background:var(--bg);overflow:hidden}
.wrap{position:absolute;left:174px;width:600px}
.eyebrow{font-size:6px;font-weight:700;letter-spacing:2px;color:var(--lime);text-transform:uppercase}
.h2{font-size:19px;font-weight:700;text-transform:uppercase;letter-spacing:.2px}

/* hero */
.hero{position:absolute;left:0;top:0;width:948px;height:437px}
.hero-photo{position:absolute;inset:0;background:radial-gradient(ellipse at 55% 30%,#4a4a4a 0%,#2f2f2f 45%,#1c1c1c 80%),#222}
.hero-photo::after{content:"";position:absolute;left:0;right:0;bottom:0;height:120px;background:linear-gradient(transparent,var(--bg))}
.nav{position:absolute;left:174px;top:12px;width:600px;display:flex;align-items:center;justify-content:space-between}
.nav-brand{display:flex;align-items:center;gap:7px;font-size:10px;font-weight:700;text-transform:uppercase;letter-spacing:.3px}
.nav-brand .mark{width:14px;height:14px;background:var(--lime)}
.nav-links{display:flex;align-items:center;gap:16px;font-size:7px;letter-spacing:1.2px;color:#cfcfcf}
.nav-links .active{color:var(--lime)}
.btn{display:inline-flex;align-items:center;justify-content:center;font-size:7.5px;font-weight:700;letter-spacing:1.2px;text-transform:uppercase}
.btn-lime{background:var(--lime);color:var(--ink)}
.btn-ghost{border:1px solid #d8d8d8;color:#fff}
.nav .btn{width:66px;height:18px}
.hero-copy{position:absolute;left:0;width:948px;top:130px;text-align:center}
.hero-copy .eyebrow{font-size:7px;letter-spacing:3px}
.hero-copy h1{font-size:39px;font-weight:800;line-height:36px;margin-top:14px;text-transform:uppercase}
.hero-copy p{font-size:10px;color:#d5d5d5;line-height:14px;margin-top:22px}
.hero-actions{display:flex;justify-content:center;gap:8px;margin-top:23px}
.hero-actions .btn{width:82px;height:29px}
.scroll-line{position:absolute;left:474px;top:400px;width:1px;height:26px;background:#555}

/* services */
.services{position:absolute;left:0;top:437px;width:948px;height:294px;border-bottom:1px solid var(--line)}
.services .head{position:absolute;top:60px;left:0;width:948px;text-align:center}
.services .h2{margin-top:6px}
.cards{position:absolute;left:174px;top:123px;width:600px;display:flex;gap:18px}
.card{width:188px;height:125px;background:var(--card);padding:20px}
.card svg{width:14px;height:14px;stroke:var(--lime);fill:none;stroke-width:1.6}
.card h3{font-size:9.5px;font-weight:700;margin-top:10px;text-transform:uppercase}
.card p{font-size:6.5px;color:var(--dim);line-height:11px;margin-top:10px}

/* about */
.about{position:absolute;left:0;top:731px;width:948px;height:342px}
.about-text{position:absolute;left:174px;top:58px;width:285px}
.about-text .h2{margin-top:8px}
.about-text p{font-size:7.2px;color:#a9a9a9;line-height:12.6px;margin-top:16px}
.about-text p+p{margin-top:12px}
.stats{display:flex;gap:8px;margin-top:20px}
.stat{width:138px;height:55px;background:var(--card);border-left:2px solid var(--lime);padding:12px}
.stat b{display:block;font-size:15px;font-weight:700}
.stat span{display:block;font-size:5.5px;letter-spacing:1px;color:var(--dim);margin-top:4px;text-transform:uppercase}
.about-figure{position:absolute;left:489px;top:48px;width:300px;height:263px;border:1px solid #3a3d25}
.about-photo{position:absolute;left:0;top:0;width:285px;height:247px;background:linear-gradient(150deg,#e8e8e8 0%,#bdbdbd 45%,#6e6e6e 100%)}

/* projects */
.projects{position:absolute;left:0;top:1073px;width:948px;height:556px;background:var(--band)}
.projects-head{position:absolute;left:174px;top:48px;width:600px;display:flex;justify-content:space-between;align-items:flex-end}
.projects-head .h2{margin-top:6px}
.view-all{font-size:7px;font-weight:700;letter-spacing:1px;display:flex;align-items:center;gap:6px;margin-bottom:3px}
.grid{position:absolute;left:174px;top:112px;width:600px;display:grid;grid-template-columns:repeat(3,192px);gap:13px 12px}
.project{position:relative;height:192px;overflow:hidden}
.project .photo{position:absolute;inset:0}
.project .photo::after{content:"";position:absolute;inset:0;background:linear-gradient(transparent 45%,rgba(10,10,10,.85))}
.project .info{position:absolute;left:16px;bottom:14px}
.project .cat{font-size:5.5px;font-weight:700;letter-spacing:1px;color:var(--lime);text-transform:uppercase}
.project h4{font-size:10px;font-weight:600;margin-top:4px}
.project .loc{font-size:6.5px;color:#a0a0a0;margin-top:4px;display:flex;align-items:center;gap:3px}
.loc svg{width:5px;height:6px;fill:none;stroke:#a0a0a0;stroke-width:1.2}

/* contact */
.contact{position:absolute;left:0;top:1629px;width:948px;height:411px;overflow:hidden}
.contact .slant{position:absolute;inset:0;width:948px;height:411px}
.contact .head{position:absolute;top:50px;left:0;width:948px;text-align:center}
.contact .h2{margin-top:6px}
.contact-info{position:absolute;left:174px;top:118px;width:285px}
.contact-info > p{font-size:9px;color:#b5b5b5;line-height:16px}
.contact-list{margin-top:24px;display:flex;flex-direction:column;gap:18px}
.contact-item{display:flex;align-items:center;gap:12px}
.contact-item .ico{width:24px;height:24px;background:var(--card);display:flex;align-items:center;justify-content:center}
.ico svg{width:11px;height:11px;fill:none;stroke:var(--lime);stroke-width:1.6}
.contact-item small{display:block;font-size:5.5px;letter-spacing:1px;color:var(--dim)}
.contact-item span{display:block;font-size:8.5px;margin-top:2px}
.form{position:absolute;left:489px;top:111px;width:285px;height:254px;background:#212121;border-top:3px solid var(--lime);padding:20px}
.form label{display:block;font-size:5.5px;letter-spacing:1px;color:var(--dim);font-weight:600}
.form .row{display:flex;gap:12px}
.form .field{flex:1;margin-bottom:14px}
.form .input{height:24px;background:#171717;border:1px solid #3a3a3a;margin-top:5px}
.form .textarea{height:60px}
.form .btn{width:245px;height:27px;margin-top:0}

/* footer */
.footer{position:absolute;left:0;top:2040px;width:948px;height:138px;background:var(--foot)}
.foot-top{position:absolute;left:174px;top:40px;width:600px;display:flex;justify-content:space-between;align-items:center}
.foot-brand{display:flex;align-items:center;gap:6px;font-size:7px;font-weight:700;text-transform:uppercase}
.foot-brand .mark{width:10px;height:10px;background:var(--lime)}
.foot-links{display:flex;gap:16px;font-size:7px;color:var(--dim)}
.foot-rule{position:absolute;left:174px;top:90px;width:600px;height:1px;background:#1f1f1f}
.foot-bottom{position:absolute;left:174px;top:106px;width:600px;display:flex;justify-content:space-between;font-size:5.5px;color:#555}
.foot-bottom div{display:flex;gap:12px}
</style>
</head>
<body>

<div class="brand-board">
  <div class="mark"></div>
  <div class="name">Gullwind Stonecut Earthworks</div>
</div>

<main class="site">

  <section class="hero">
    <div class="hero-photo" role="img" aria-label="Dark monochrome photo of a large excavator against a mountain backdrop"></div>
    <nav class="nav">
      <div class="nav-brand"><span class="mark"></span>Gullwind Stonecut</div>
      <div class="nav-links">
        <span class="active">HOME</span><span>SERVICES</span><span>ABOUT</span><span>PROJECTS</span>
        <span class="btn btn-lime">Get Quote</span>
      </div>
    </nav>
    <div class="hero-copy">
      <div class="eyebrow">Perth, Western Australia</div>
      <h1>Precision<br>Earthworks</h1>
      <p>Professional excavation and site preparation services.<br>Modern fleet. Reliable operators. Exceptional results.</p>
      <div class="hero-actions">
        <span class="btn btn-lime">Our Work</span>
        <span class="btn btn-ghost">Contact Us</span>
      </div>
    </div>
    <div class="scroll-line"></div>
  </section>

  <section class="services">
    <div class="head">
      <div class="eyebrow">What We Do</div>
      <h2 class="h2">Our Core Services</h2>
    </div>
    <div class="cards">
      <article class="card">
        <svg viewBox="0 0 16 16"><rect x="1" y="4" width="9" height="7"/><path d="M10 6h3l2 3v2h-5z"/><circle cx="4" cy="12.5" r="1.5"/><circle cx="12" cy="12.5" r="1.5"/></svg>
        <h3>Site Clearing</h3>
        <p>Complete removal of vegetation, debris, and structures to prepare your land for development.</p>
      </article>
      <article class="card">
        <svg viewBox="0 0 16 16"><path d="M14 2l-7 7"/><path d="M6 8l2 2-3 3-3-1-1-3 3-3z"/><path d="M12 1l3 3"/></svg>
        <h3>Excavation</h3>
        <p>Precision digging for pools, foundations, and trenches across the Perth metro area.</p>
      </article>
      <article class="card">
        <svg viewBox="0 0 16 16"><path d="M2 12h12"/><path d="M3 12a5 5 0 0 1 10 0"/><path d="M7 7V4h2v3"/></svg>
        <h3>Final Trim</h3>
        <p>Detailed earth shaping, leveling, and preparation for driveways, slabs, and landscaping.</p>
      </article>
    </div>
  </section>

  <section class="about">
    <div class="about-text">
      <div class="eyebrow">About Us</div>
      <h2 class="h2">Built On Solid Ground</h2>
      <p>Gullwind Stonecut Earthworks was established with a singular vision: to provide Perth with a modern, reliable, and precise earthmoving service. We stepped away from the "old school" rough-and-ready approach to offer a service that prioritizes accuracy, safety, and client communication.</p>
      <p>We understand that earthworks are the foundation of every great project. If the ground isn't right, nothing else will be. That's why we invest in the latest machinery and ensure our operators are highly skilled.</p>
      <div class="stats">
        <div class="stat"><b>100%</b><span>Safety Record</span></div>
        <div class="stat"><b>Perth</b><span>Metro Wide</span></div>
      </div>
    </div>
    <div class="about-figure">
      <div class="about-photo" role="img" aria-label="Black and white photo of an excavator arm and bucket against a cloudy sky"></div>
    </div>
  </section>

  <section class="projects">
    <div class="projects-head">
      <div>
        <div class="eyebrow">Our Portfolio</div>
        <h2 class="h2">Featured Projects</h2>
      </div>
      <div class="view-all">VIEW ALL WORK
        <svg width="7" height="6" viewBox="0 0 7 6" fill="none" stroke="#fff" stroke-width="1"><path d="M0 3h6M4 1l2 2-2 2"/></svg>
      </div>
    </div>
    <div class="grid">
      <article class="project">
        <div class="photo" role="img" aria-label="Yellow excavator working in a brown dirt pit" style="background:linear-gradient(160deg,#6b5a45,#4a3e30 60%,#2e2820)"></div>
        <div class="info"><div class="cat">Commercial</div><h4>Site Remediation</h4><div class="loc"><svg viewBox="0 0 6 8"><path d="M3 7.5S.6 4.8.6 3a2.4 2.4 0 0 1 4.8 0C5.4 4.8 3 7.5 3 7.5z"/></svg>Scarborough, WA</div></div>
      </article>
      <article class="project">
        <div class="photo" role="img" aria-label="Excavator digging beside trees under a blue sky" style="background:linear-gradient(170deg,#3d5270,#3a3f3a 55%,#2b2722)"></div>
        <div class="info"><div class="cat">Residential</div><h4>Pool Excavation</h4><div class="loc"><svg viewBox="0 0 6 8"><path d="M3 7.5S.6 4.8.6 3a2.4 2.4 0 0 1 4.8 0C5.4 4.8 3 7.5 3 7.5z"/></svg>Cottesloe, WA</div></div>
      </article>
      <article class="project">
        <div class="photo" role="img" aria-label="Excavator clearing scrub near a forest edge" style="background:linear-gradient(170deg,#6e7a84,#3e4a3a 55%,#262a22)"></div>
        <div class="info"><div class="cat">Agricultural</div><h4>Land Clearing</h4><div class="loc"><svg viewBox="0 0 6 8"><path d="M3 7.5S.6 4.8.6 3a2.4 2.4 0 0 1 4.8 0C5.4 4.8 3 7.5 3 7.5z"/></svg>Swan Valley, WA</div></div>
      </article>
      <article class="project">
        <div class="photo" role="img" aria-label="Long trench cut through dirt beside a machine" style="background:linear-gradient(170deg,#8b8a80,#6a5d4c 50%,#3a3128)"></div>
        <div class="info"><div class="cat">Civil</div><h4>Trenching</h4><div class="loc"><svg viewBox="0 0 6 8"><path d="M3 7.5S.6 4.8.6 3a2.4 2.4 0 0 1 4.8 0C5.4 4.8 3 7.5 3 7.5z"/></svg>Balcatta, WA</div></div>
      </article>
      <article class="project">
        <div class="photo" role="img" aria-label="Orange excavator on a gravel driveway beside a house among pines" style="background:linear-gradient(170deg,#7a7c78,#4d4a44 55%,#2c2a27)"></div>
        <div class="info"><div class="cat">Residential</div><h4>Driveway Prep</h4><div class="loc"><svg viewBox="0 0 6 8"><path d="M3 7.5S.6 4.8.6 3a2.4 2.4 0 0 1 4.8 0C5.4 4.8 3 7.5 3 7.5z"/></svg>Hillarys, WA</div></div>
      </article>
      <article class="project">
        <div class="photo" role="img" aria-label="Yellow excavator tearing down a structure in dust" style="background:linear-gradient(170deg,#a3a39e,#6a645a 50%,#3a3229)"></div>
        <div class="info"><div class="cat">Demolition</div><h4>Demolition</h4><div class="loc"><svg viewBox="0 0 6 8"><path d="M3 7.5S.6 4.8.6 3a2.4 2.4 0 0 1 4.8 0C5.4 4.8 3 7.5 3 7.5z"/></svg>Subiaco, WA</div></div>
      </article>
    </div>
  </section>

  <section class="contact">
    <svg class="slant" viewBox="0 0 948 411" aria-hidden="true"><polygon points="672,0 948,0 948,411 590,411" fill="#1d1d1d"/></svg>
    <div class="head">
      <div class="eyebrow">Get In Touch</div>
      <h2 class="h2">Start Your Project</h2>
    </div>
    <div class="contact-info">
      <p>Ready to break ground? We provide free, no-obligation quotes for all residential and commercial earthworks projects in Perth.</p>
      <div class="contact-list">
        <div class="contact-item">
          <div class="ico"><svg viewBox="0 0 12 12"><path d="M2 1h2.5l1 3-1.5 1a7 7 0 0 0 3 3l1-1.5 3 1V10a1 1 0 0 1-1 1A10 10 0 0 1 1 2a1 1 0 0 1 1-1z"/></svg></div>
          <div><small>PHONE</small><span>+61 400 555 019</span></div>
        </div>
        <div class="contact-item">
          <div class="ico"><svg viewBox="0 0 12 12"><rect x="1" y="2.5" width="10" height="7"/><path d="M1 3l5 4 5-4"/></svg></div>
          <div><small>EMAIL</small><span>hello@gullwindstonecut.com.au</span></div>
        </div>
        <div class="contact-item">
          <div class="ico"><svg viewBox="0 0 12 12"><path d="M6 11S2 7 2 4.6a4 4 0 0 1 8 0C10 7 6 11 6 11z"/><circle cx="6" cy="4.6" r="1.4"/></svg></div>
          <div><small>LOCATION</small><span>Perth, Western Australia</span></div>
        </div>
      </div>
    </div>
    <form class="form">
      <div class="row">
        <div class="field"><label>NAME</label><div class="input"></div></div>
        <div class="field"><label>PHONE</label><div class="input"></div></div>
      </div>
      <div class="field"><label>EMAIL</label><div class="input"></div></div>
      <div class="field"><label>PROJECT DETAILS</label><div class="input textarea"></div></div>
      <div class="btn btn-lime">Send Enquiry</div>
    </form>
  </section>

  <footer class="footer">
    <div class="foot-top">
      <div class="foot-brand"><span class="mark"></span>Gullwind Stonecut</div>
      <div class="foot-links"><span>Home</span><span>Services</span><span>About</span><span>Projects</span><span>Contact</span></div>
    </div>
    <div class="foot-rule"></div>
    <div class="foot-bottom">
      <span>© 2026 Gullwind Stonecut Earthworks.</span>
      <div><span>Privacy</span><span>Terms</span></div>
    </div>
  </footer>

</main>
</body>
</html>
```